Brenner Business Cards

Front of business card will have logo, name, address, & telephone number. Back of card will have a list of services provided - Roads, Substation Pads, Temporary Pads, Site Pads, Land Leveling, Powerline Row Cleaning, Land Clearing, Gates, Fencing, Construction Entrances, Excavation, Trenching, Underground Utilities, Directional Boring, Pile Driving. We are a construction company that uses heavy equipment like bulldozers, motor graders/blades, dump trucks, backhoes, hydro axes, & skid loaders. We build roads, pads, & install electric utility lines & waterlines underground. This logo is new. The word "Construction" can be smaller as uploaded 2 example edited logos. We will be using this card design for many employees.
Target Market(s)
Industrial Electric Powerline, Wind Turbine, Solar Panel, & Water Utility companies.
Contact Information for Business Card
Name/Position - Danny Brenner - Owner
Address: 4837 FM 952
Carlow, OK 79284
Phone number - (555) 518-2906

```html
<!DOCTYPE html>
<html lang="en">
<head>
<meta charset="utf-8">
<title>Brenner Construction Business Cards</title>
<link href="https://fonts.googleapis.com/css2?family=Roboto:wght@400;500;700&display=swap" rel="stylesheet">
<style>
  :root {
    --backdrop: #2b2b2c;
    --maroon: #5a1d2e;
    --maroon-light: #6b2a3d;
    --maroon-dark: #4a1624;
    --paper: #ffffff;
    --ink-grey: #6e6e6e;
    --ink-white: #ffffff;
  }
  * { margin: 0; padding: 0; box-sizing: border-box; }
  html, body {
    width: 1200px; height: 929px; overflow: hidden;
    background: var(--backdrop);
    font-family: "Roboto", sans-serif;
  }
  .canvas {
    position: relative; width: 1200px; height: 929px;
    display: flex; flex-direction: column; align-items: center; justify-content: center; gap: 56px;
  }
  .card {
    width: 580px; height: 332px; border-radius: 18px; position: relative; overflow: hidden;
  }
  /* Services side */
  .card-services {
    background: linear-gradient(135deg, var(--maroon-dark) 0%, var(--maroon) 50%, var(--maroon-light) 100%);
    color: var(--ink-white);
    display: flex; flex-direction: column; align-items: center; padding-top: 58px;
  }
  .brand {
    display: flex; align-items: center; gap: 12px;
    font-weight: 700; letter-spacing: 0.06em; text-transform: uppercase;
  }
  .brand-mark { width: 22px; height: 22px; border-radius: 50%; background: currentColor; flex: none; }
  .card-services .brand { font-size: 34px; }
  .services-pill {
    margin-top: 20px; background: var(--paper); color: var(--maroon);
    font-size: 15px; font-weight: 500; padding: 4px 22px; border-radius: 6px;
  }
  .services-list {
    margin-top: 18px; list-style: none; text-align: center;
    font-size: 15px; line-height: 1.55; white-space: nowrap;
  }
  .bullet { font-size: 11px; vertical-align: 1px; margin: 0 4px; }
  /* Contact side */
  .card-contact {
    background: var(--paper);
    display: flex; align-items: center; padding: 0 30px 0 36px;
  }
  .card-contact .brand {
    color: var(--maroon); font-size: 22px; flex-direction: column; gap: 10px; width: 200px; text-align: center; flex: none;
  }
  .divider { width: 1.5px; height: 120px; background: var(--maroon); margin: 0 24px; flex: none; }
  .contact { white-space: nowrap; }
  .contact-name { color: var(--maroon); font-size: 22px; font-weight: 700; }
  .contact-role { color: var(--ink-grey); font-size: 14px; font-weight: 500; margin-bottom: 20px; }
  .contact-line { display: flex; align-items: center; gap: 8px; color: var(--ink-grey); font-size: 14px; line-height: 1.7; }
  .contact-line svg { width: 13px; height: 13px; fill: var(--maroon); flex: none; }
</style>
</head>
<body>
<main class="canvas">
  <section class="card card-services">
    <div class="brand"><span class="brand-mark"></span>Brenner Construction</div>
    <div class="services-pill">Our Services</div>
    <ul class="services-list">
      <li><span class="bullet">●</span>Roads, Substation Pads<span class="bullet">●</span>Temporary Pads, Site Pads</li>
      <li><span class="bullet">●</span>Land Leveling, Powerline Row Cleaning<span class="bullet">●</span>Land Clearing<span class="bullet">●</span>Gates<span class="bullet">●</span>Fencing</li>
      <li><span class="bullet">●</span>Construction Entrances<span class="bullet">●</span>Excavation<span class="bullet">●</span>Trenching</li>
      <li><span class="bullet">●</span>Underground Utilities<span class="bullet">●</span>Directional Boring<span class="bullet">●</span>Pile Driving</li>
    </ul>
  </section>

  <section class="card card-contact">
    <div class="brand"><span class="brand-mark"></span>Brenner Construction</div>
    <div class="divider"></div>
    <div class="contact">
      <div class="contact-name">Danny Brenner</div>
      <div class="contact-role">Owner</div>
      <div class="contact-line">
        <svg viewBox="0 0 24 24" aria-hidden="true"><path d="M6.6 10.8a15.1 15.1 0 0 0 6.6 6.6l2.2-2.2a1 1 0 0 1 1-.25 11.4 11.4 0 0 0 3.6.57 1 1 0 0 1 1 1V20a1 1 0 0 1-1 1A17 17 0 0 1 3 4a1 1 0 0 1 1-1h3.5a1 1 0 0 1 1 1c0 1.25.2 2.45.57 3.570a1 1 0 0 1-.25 1z"/></svg>
        (555) 518-2906
      </div>
      <div class="contact-line">
        <svg viewBox="0 0 24 24" aria-hidden="true"><path d="M12 2a7 7 0 0 0-7 7c0 5.25 7 13 7 13s7-7.75 7-13a7 7 0 0 0-7-7zm0 9.5A2.5 2.5 0 1 1 12 6.5a2.5 2.5 0 0 1 0 5z"/></svg>
        4837 FM 952 Carlow, OK 79284
      </div>
    </div>
  </section>
</main>
</body>
</html>
```